Business Card Design for Real Estate Company

I am looking for a business card design that will catch my client's attention.

Industry/Entity Type

Business

Requirements
Must have
• Please have the following information in the business card design. You can substitute the "Office, Mobile, email, and web" with an icon or some other design you may think will go well with the business card.

Derek Osmund
482 W. Fenwick St., Suite 310
Pasadena, CA 91348
Office: 626.748.1196
Mobile: 626.913.4071
email: Derek@CrestviewPropertyWalk.example
web: www.CrestviewPropertyWalk.example

```html
<!DOCTYPE html>
<html lang="en">
<head>
<meta charset="utf-8">
<title>Crestview Property Walk — Business Card</title>
<link rel="stylesheet" href="https://fonts.googleapis.com/css2?family=Cabin:wght@400&family=Didact+Gothic&display=swap">
<style>
  :root {
    --backdrop: #3b2f29;
    --card-light: #ffffff;
    --card-edge: #efe9e9;
    --ink-brown: #4a3b2d;
    --divider: #d9d2d2;
    --accent-leaf: #8fb23a;
  }
  * { margin: 0; padding: 0; box-sizing: border-box; }
  html, body {
    width: 1200px;
    height: 822px;
    overflow: hidden;
    background: var(--backdrop);
  }
  .canvas {
    position: relative;
    width: 1200px;
    height: 822px;
  }
  .card {
    position: absolute;
    background: radial-gradient(ellipse at 45% 40%, var(--card-light) 0%, var(--card-edge) 100%);
    box-shadow: 0 6px 18px rgba(0,0,0,0.45);
  }
  .card--front {
    left: 48px; top: 32px;
    width: 619px; height: 347px;
    display: flex;
    align-items: center;
    justify-content: center;
  }
  .card--back {
    left: 539px; top: 425px;
    width: 613px; height: 344px;
  }
  .brand {
    display: flex;
    align-items: center;
    gap: 14px;
    color: var(--ink-brown);
    font-family: "Cabin", sans-serif;
    font-weight: 400;
  }
  .brand__dot {
    flex: none;
    border-radius: 50%;
    background: var(--accent-leaf);
  }
  .card--front .brand { margin-top: -12px; }
  .card--front .brand__dot { width: 30px; height: 30px; }
  .card--front .brand__name { font-size: 40px; letter-spacing: 0.5px; }

  .card--back .brand {
    position: absolute;
    left: 30px; top: 140px;
    width: 250px;
    gap: 10px;
  }
  .card--back .brand__dot { width: 18px; height: 18px; }
  .card--back .brand__name { font-size: 22px; line-height: 1.15; }

  .card__divider {
    position: absolute;
    left: 302px; top: 59px;
    width: 1px; height: 219px;
    background: var(--divider);
  }
  .contact {
    position: absolute;
    left: 321px; top: 82px;
    color: var(--ink-brown);
    font-family: "Cabin", sans-serif;
    font-size: 13.5px;
    line-height: 19.4px;
  }
  .contact__name {
    font-family: "Didact Gothic", sans-serif;
    font-size: 20px;
    line-height: 24px;
    margin-bottom: 2px;
  }
  .contact__line { white-space: nowrap; }
</style>
</head>
<body>
<main class="canvas">
  <section class="card card--front" aria-label="Card front">
    <div class="brand">
      <span class="brand__dot" aria-hidden="true"></span>
      <span class="brand__name">Crestview Property Walk</span>
    </div>
  </section>

  <section class="card card--back" aria-label="Card back">
    <div class="brand">
      <span class="brand__dot" aria-hidden="true"></span>
      <span class="brand__name">Crestview<br>Property Walk</span>
    </div>
    <div class="card__divider" aria-hidden="true"></div>
    <address class="contact" style="font-style:normal">
      <div class="contact__name">Derek Osmund</div>
      <div class="contact__line">482 W. Fenwick St., Suite 310</div>
      <div class="contact__line">Pasadena, CA 91348</div>
      <div class="contact__line">Office: 626.748.1196</div>
      <div class="contact__line">Mobile: 626.913.4071</div>
      <div class="contact__line">email: Derek@CrestviewPropertyWalk.example</div>
      <div class="contact__line">web: www.CrestviewPropertyWalk.example</div>
    </address>
  </section>
</main>
</body>
</html>
```